Business Card Design Project

Design a business card for a new entity that is in the OTC (over-the-counter-derivative brokering business-Financial Services.
The card should be clean a professional looking. We encourage designers to think pro-actively, fresh and innovative, but also keep in mind that only 2 things are important. a)that the card look professional b)that it is somehow memorable.

We have a new logo which we will upload and will want the Trident symbol in the logo to be raised OR not have the symbol raised and plan on having the word " BROKERAGE SERVICES" raised that stands out and will look sharp.

Along with uploading the new logo which MUST be incorperated, I am also going to upload 3 different business cards of other businesses to use only as guild-lines since I think they are clean and professional looking BUT I encourage all to be pro-active and creative on their own.

Industry/Entity Type

Business

Requirements
Must have
• 1. MUST HAVE THE NEW LOGO WHICH WILL BE UPLOADED
2. MUST HAVE A VERSION SIMILAR TO THE 3 DIFFERENT BUSINESS CARDS I WILL UPLOAD, BUT EACH DESIGNER MUST ONLY THESE THIS FORMAT AS A BACK-UP AND BE CREATIVE ON THEIR OWN FIRST. ALSO WHEN LOOKING AT THE CARDS WHICH I UPLOAD TO USE AS A GUILD-LINE KEEP IN MIND THAT THESE ARE PINNACLE 300 COMPANIES SO DO NOT MIMIC ONLY USE FOR IDEAS.
Nice to have
• these are the 3 different other biz cards to look at for some reference

```html
<!DOCTYPE html>
<html lang="en">
<head>
<meta charset="utf-8">
<title>Meridian Brokerage Services – Business Card</title>
<link href="https://fonts.googleapis.com/css2?family=Play:wght@400;700&display=swap" rel="stylesheet">
<style>
  :root {
    --stage: #4a4a4a;
    --card: #ffffff;
    --ink: #2b2b2b;
    --ink-soft: #3a3a3a;
    --gold: #d6a93a;
    --gold-light: #efc857;
    --gold-deep: #c99a2e;
    --tag: #b58a2a;
    --white: #ffffff;
  }
  * { box-sizing: border-box; margin: 0; padding: 0; }
  html, body { width: 1200px; height: 900px; overflow: hidden; }
  body {
    background: var(--stage);
    font-family: "Play", sans-serif;
    position: relative;
  }
  .card {
    position: absolute;
    top: 300px;
    width: 524px;
    height: 299px;
    border-radius: 18px;
    background: var(--card);
    overflow: hidden;
    box-shadow: 0 2px 6px rgba(0,0,0,.25);
  }
  .card--front { left: 58px; }
  .card--back { left: 617px; }

  /* Brand lockup */
  .brand { display: flex; align-items: center; gap: 12px; }
  .brand__mark {
    width: 22px; height: 22px;
    background: var(--ink-soft);
  }
  .brand__name {
    font-weight: 700;
    color: var(--ink-soft);
    letter-spacing: 3px;
    line-height: 1;
  }
  .tagline {
    color: var(--tag);
    letter-spacing: 4.5px;
    font-size: 13px;
    text-transform: uppercase;
  }

  /* Front */
  .front__brand { position: absolute; left: 48px; top: 42px; }
  .front__brand .brand__name { font-size: 38px; }
  .front__tagline { position: absolute; left: 152px; top: 89px; }
  .contact-band {
    position: absolute; left: 0; right: 0; top: 150px; bottom: 0;
    background: linear-gradient(100deg, var(--gold-deep) 0%, var(--gold-light) 55%, var(--gold) 100%);
  }
  .contact-band__notch {
    position: absolute; left: 70px; top: 0;
  }
  .person { position: absolute; left: 48px; top: 28px; color: var(--ink); }
  .person__name { font-size: 17px; }
  .person__role { font-size: 12px; margin-left: 6px; }
  .person__lines { margin-top: 8px; font-size: 11.5px; line-height: 16px; }
  .person__lines .label { color: var(--white); }
  .person__web { margin-top: 12px; font-size: 14px; font-weight: 700; }
  .divider {
    position: absolute; left: 310px; top: 30px; width: 1px; height: 88px;
    background: var(--ink);
  }
  .office {
    position: absolute; left: 330px; top: 28px;
    font-size: 11.5px; line-height: 16px; color: var(--ink);
  }
  .office__phones { margin-top: 14px; }
  .office .label { color: var(--white); }

  /* Back */
  .back__brand {
    position: absolute; left: 0; right: 0; top: 160px;
    text-align: center;
  }
  .back__brand .brand { justify-content: center; }
  .back__brand .brand__name { font-size: 42px; }
  .back__tagline { margin-top: 8px; }
  .back__web {
    position: absolute; left: 0; right: 0; top: 252px;
    text-align: center; font-size: 12px; letter-spacing: 4px; color: var(--ink);
  }
</style>
</head>
<body>

<section class="card card--front">
  <div class="front__brand brand">
    <span class="brand__mark"></span>
    <span class="brand__name">MERIDIAN</span>
  </div>
  <div class="front__tagline tagline">Brokerage Services</div>

  <div class="contact-band">
    <svg class="contact-band__notch" width="34" height="18" viewBox="0 0 34 18" aria-hidden="true">
      <polygon points="0,0 34,0 17,17" fill="#ffffff"/>
    </svg>
    <div class="person">
      <div><span class="person__name">John Doe</span><span class="person__role">Manager</span></div>
      <div class="person__lines">
        <div><span class="label">Mobile:</span> 000 000 000</div>
        <div><span class="label">Email:</span> john@meridianbrokerage.com</div>
      </div>
      <div class="person__web">www.MeridianBrokerage.com</div>
    </div>
    <div class="divider"></div>
    <div class="office">
      <div>00 Your Street</div>
      <div>000000 000 000 0000</div>
      <div>PO Box 000</div>
      <div class="office__phones">
        <div><span class="label">Ph:</span> +00 7 0000 0000</div>
        <div><span class="label">Fax:</span> + 00 7 0000 0000</div>
      </div>
    </div>
  </div>
</section>

<section class="card card--back">
  <div class="back__brand">
    <div class="brand">
      <span class="brand__mark"></span>
      <span class="brand__name">MERIDIAN</span>
    </div>
    <div class="back__tagline tagline">Brokerage Services</div>
  </div>
  <div class="back__web">www.MeridianBrokerage.com</div>
</section>

</body>
</html>
```